"Wellenhafen" private practice for physiotherapy

we are looking for a flyer design for a private practice for physiotherapy. the name of the practice is "Wellenhafen".
Treatments such as: manual therapy, manual lymphatic drainage, classic massage, sectoral alternative practitioners are offered

The flyers should be double-sided and the format DIN long (105x210 mm)

Font styles to use
Serif

Colors
0094D4
00A9DD
6FCCEA
C7EBF8
E9F6FB

Requirements
Must have
• Wellenhafen, Lindenweg 17, 04719 Birkenfelde / Wellenhafen-praxis-beispiel.de / Tel. 03471 5820317

```html
<!DOCTYPE html>
<html lang="de">
<head>
<meta charset="utf-8">
<title>Wellenhafen – Flyer DIN lang</title>
<link rel="stylesheet" href="https://fonts.googleapis.com/css2?family=Tinos&family=Poppins:wght@400;500&display=swap">
<style>
  :root {
    --blue-deep: #0094D4;
    --blue: #00A9DD;
    --blue-soft: #6FCCEA;
    --blue-pale: #C7EBF8;
    --blue-mist: #E9F6FB;
    --ink: #2b2b2b;
    --text: #444;
    --stage: #eef1f3;
  }
  * { box-sizing: border-box; margin: 0; padding: 0; }
  html, body { width: 878px; height: 1200px; overflow: hidden; background: var(--stage); }
  .canvas { position: relative; width: 878px; height: 1200px; }
  .flyer {
    position: absolute; top: 200px; width: 400px; height: 800px; overflow: hidden;
    background: linear-gradient(180deg, #fff 0%, #fff 45%, var(--blue-mist) 70%, var(--blue-pale) 100%);
    box-shadow: 0 6px 18px rgba(0,0,0,.12);
    font-family: "Poppins", sans-serif; text-align: center; color: var(--text);
  }
  .flyer--front { left: 24px; }
  .flyer--back { left: 454px; }
  .brand {
    position: absolute; left: 0; right: 0; top: 46px;
    font-family: "Poppins", sans-serif; font-weight: 500; font-size: 30px; line-height: 38px;
    color: var(--blue);
  }
  .tagline { position: absolute; left: 0; right: 0; top: 88px; font-size: 15px; color: #444; }
  .photo-band {
    position: absolute; left: 0; top: 114px; width: 400px; height: 244px;
    background: linear-gradient(180deg, #f4f5f6 0%, #e6e9ec 40%, #8aa9c4 70%, #2f5f8f 85%, #f7f8fa 100%);
  }
  .offer-title {
    position: absolute; left: 0; right: 0; top: 372px;
    font-family: "Tinos", serif; font-weight: 400; font-size: 44px; line-height: 50px; color: var(--ink);
  }
  .services { position: absolute; left: 80px; right: 80px; top: 428px; list-style: none; }
  .services li { font-size: 17px; line-height: 23px; padding: 5px 0 6px; border-bottom: 1px solid rgba(0,148,212,.12); }
  .services li:last-child { border-bottom: none; }
  .about {
    position: absolute; left: 58px; right: 58px; top: 466px;
    font-size: 9.6px; line-height: 16.7px; color: #333;
  }
  .circles { position: absolute; left: 0; top: 130px; width: 400px; height: 320px; }
  .wave { position: absolute; left: 0; bottom: 0; width: 400px; height: 230px; }
  .contact { position: absolute; left: 0; right: 0; top: 682px; color: #fff; }
  .contact .footer-name { font-family: "Poppins", sans-serif; font-weight: 500; font-size: 25px; line-height: 32px; margin-bottom: 4px; }
  .contact p { font-size: 11.5px; line-height: 15px; }
  .contact .row { display: inline-flex; align-items: center; gap: 3px; }
  .contact svg { width: 12px; height: 12px; }
  .contact .gap { margin-top: 2px; }
</style>
</head>
<body>
<div class="canvas">

  <svg width="0" height="0" style="position:absolute">
    <defs>
      <linearGradient id="waveMain" x1="0" y1="0" x2="0" y2="1">
        <stop offset="0" stop-color="#6FCCEA"/>
        <stop offset=".35" stop-color="#00A9DD"/>
        <stop offset="1" stop-color="#0094D4"/>
      </linearGradient>
      <linearGradient id="waveLight" x1="0" y1="0" x2="1" y2="0">
        <stop offset="0" stop-color="#00A9DD"/>
        <stop offset="1" stop-color="#6FCCEA"/>
      </linearGradient>
    </defs>
  </svg>

  <section class="flyer flyer--front">
    <h1 class="brand">Wellenhafen</h1>
    <p class="tagline">Privatpraxis für Physiotherapie</p>
    <div class="photo-band" role="img" aria-label="Foto: Therapeut begleitet einen älteren Patienten bei einer Übung auf der Matte"></div>
    <h2 class="offer-title">We Offer</h2>
    <ul class="services">
      <li>Manuelle Therapie</li>
      <li>Manuelle Lymph drainage</li>
      <li>Physiotherapie</li>
      <li>Sektoraler Heilpraktiker Physiotherapie.</li>
    </ul>
    <svg class="wave" viewBox="0 0 400 230" preserveAspectRatio="none" aria-hidden="true">
      <path d="M0 14 C90 -6 200 70 300 60 C350 55 385 30 400 10 L400 230 L0 230Z" fill="url(#waveLight)"/>
      <path d="M0 26 C90 8 190 84 300 78 C350 74 385 50 400 30 L400 230 L0 230Z" fill="#fff" opacity=".85"/>
      <path d="M0 34 C90 16 190 92 300 86 C350 82 385 60 400 40 L400 230 L0 230Z" fill="url(#waveMain)"/>
    </svg>
    <div class="contact">
      <div class="footer-name">Wellenhafen</div>
      <p><span class="row"><svg viewBox="0 0 24 24" fill="none" stroke="#fff" stroke-width="2"><circle cx="12" cy="12" r="10"/><path d="M12 17s-4-4-4-7a4 4 0 0 1 8 0c0 3-4 7-4 7z"/></svg>Lindenweg 17, 04719</span><br>Birkenfelde</p>
      <p class="gap"><span class="row"><svg viewBox="0 0 24 24" fill="none" stroke="#fff" stroke-width="2"><circle cx="12" cy="12" r="10"/><circle cx="12" cy="12" r="5"/></svg>Wellenhafen-praxis-beispiel.de</span></p>
      <p class="gap"><span class="row"><svg viewBox="0 0 24 24" fill="none" stroke="#fff" stroke-width="2"><circle cx="12" cy="12" r="10"/><path d="M9 7l2 3-1.5 1.5a7 7 0 0 0 3 3L14 13l3 2-1 2c-4 0-9-5-9-9z"/></svg>03471 5820317</span></p>
    </div>
  </section>

  <section class="flyer flyer--back">
    <h1 class="brand">Wellenhafen</h1>
    <p class="tagline">Privatpraxis für Physiotherapie</p>
    <svg class="circles" viewBox="0 0 400 320" role="img" aria-label="Zwei runde Fotos: Knie-Behandlung am Patienten und Therapeutin bei einer Dehnübung mit einer Patientin">
      <defs>
        <linearGradient id="photoA" x1="0" y1="0" x2="1" y2="1">
          <stop offset="0" stop-color="#d9eef7"/><stop offset=".5" stop-color="#6f9fc9"/><stop offset="1" stop-color="#2c4f78"/>
        </linearGradient>
        <linearGradient id="photoB" x1="0" y1="0" x2="0" y2="1">
          <stop offset="0" stop-color="#f1f2f4"/><stop offset=".5" stop-color="#c9cfe0"/><stop offset="1" stop-color="#7a86b0"/>
        </linearGradient>
      </defs>
      <circle cx="298" cy="160" r="142" fill="url(#photoB)"/>
      <circle cx="88" cy="150" r="96" fill="url(#photoA)"/>
      <path d="M160 40 A160 160 0 0 1 420 70" fill="none" stroke="#00A9DD" stroke-width="1.3"/>
      <path d="M405 240 A160 160 0 0 1 225 310" fill="none" stroke="#00A9DD" stroke-width="1.3"/>
      <path d="M40 55 A108 108 0 0 1 70 45" fill="none" stroke="#00A9DD" stroke-width="1.3"/>
      <path d="M0 200 A108 108 0 0 0 140 246" fill="none" stroke="#00A9DD" stroke-width="1.3"/>
    </svg>
    <p class="about">Es ist seit langem bekannt, dass ein Leser beim Betrachten des Layouts durch den lesbaren Inhalt einer Seite abgelenkt wird. Der Punkt bei der Verwendung von Lorem Ipsum ist, dass es eine mehr oder weniger normale Verteilung von Buchstaben hat, im Gegensatz zu "Inhalt hier, Inhalt hier", wodurch es wie lesbares Englisch aussieht. Kinderschuhen stecken.</p>
    <svg class="wave" viewBox="0 0 400 230" preserveAspectRatio="none" aria-hidden="true">
      <path d="M0 14 C90 -6 200 70 300 60 C350 55 385 30 400 10 L400 230 L0 230Z" fill="url(#waveLight)"/>
      <path d="M0 26 C90 8 190 84 300 78 C350 74 385 50 400 30 L400 230 L0 230Z" fill="#fff" opacity=".85"/>
      <path d="M0 34 C90 16 190 92 300 86 C350 82 385 60 400 40 L400 230 L0 230Z" fill="url(#waveMain)"/>
    </svg>
    <div class="contact">
      <div class="footer-name">Wellenhafen</div>
      <p><span class="row"><svg viewBox="0 0 24 24" fill="none" stroke="#fff" stroke-width="2"><circle cx="12" cy="12" r="10"/><path d="M12 17s-4-4-4-7a4 4 0 0 1 8 0c0 3-4 7-4 7z"/></svg>Lindenweg 17, 04719</span><br>Birkenfelde</p>
      <p class="gap"><span class="row"><svg viewBox="0 0 24 24" fill="none" stroke="#fff" stroke-width="2"><circle cx="12" cy="12" r="10"/><circle cx="12" cy="12" r="5"/></svg>Wellenhafen-praxis-beispiel.de</span></p>
      <p class="gap"><span class="row"><svg viewBox="0 0 24 24" fill="none" stroke="#fff" stroke-width="2"><circle cx="12" cy="12" r="10"/><path d="M9 7l2 3-1.5 1.5a7 7 0 0 0 3 3L14 13l3 2-1 2c-4 0-9-5-9-9z"/></svg>03471 5820317</span></p>
    </div>
  </section>

</div>
</body>
</html>
```